Business card

would like a double sided business card made up with my logos provided.
Prefer card to have black background and to use the black logos, with matching blue writing for the text.
One side to just be the logo, (Try to use both the black logos)
the other side to have the logo and also my credentials/business information.

Covering all aspects of Carpentry and Building Services

Marcus Thelwin
Qualified Carpenter
Mob: 0417263985
Email: rkt.joinery@fernmail.example
ABN: 47 619 283 504

Industry/Entity Type

Business

Contact Information for Business Card

Marcus Thelwin
Qualified Carpenter
Mob: 0417263985
ABN: 47 619 283 504

Requirements
Must have
• Please try to use both the black logos and incorporate into the card.

```html
<!DOCTYPE html>
<html lang="en">
<head>
<meta charset="utf-8">
<title>RKT Joinery – Business Card</title>
<link rel="stylesheet" href="https://fonts.googleapis.com/css2?family=Arimo:wght@400;700&family=Raleway:wght@300;400&display=swap">
<style>
  :root {
    --card-black: #0c0c0d;
    --card-black-hi: #1c1c1f;
    --brand-blue: #2a9fd2;
    --brand-blue-dark: #1a7fb0;
    --text-white: #f4f4f4;
    --stage: #d8d3cb;
  }
  * { box-sizing: border-box; margin: 0; padding: 0; }
  html, body { width: 1200px; height: 858px; overflow: hidden; }
  body {
    background: var(--stage);
    font-family: "Arimo", Arial, sans-serif;
    position: relative;
  }
  .card {
    position: absolute;
    background: linear-gradient(150deg, var(--card-black-hi) 0%, var(--card-black) 55%);
    color: var(--text-white);
    overflow: hidden;
    box-shadow: 0 18px 40px rgba(0,0,0,.35);
  }
  .card__band {
    position: absolute; left: 0; right: 0; bottom: 0;
    background: linear-gradient(180deg, var(--brand-blue), var(--brand-blue-dark));
    border-top: 3px solid var(--card-black);
  }
  .card__band::before {
    content: ""; position: absolute; left: 0; right: 0; top: -6px;
    height: 2px; background: #e8e8e8;
  }
  .brand-name {
    font-family: "Raleway", sans-serif;
    font-weight: 300;
    color: var(--text-white);
    letter-spacing: .06em;
    white-space: nowrap;
    display: flex; align-items: center;
  }
  .brand-mark {
    display: inline-block; background: var(--brand-blue);
    flex: none;
  }
  .brand-sub {
    font-family: "Raleway", sans-serif;
    font-weight: 400;
    color: var(--brand-blue);
    text-transform: uppercase;
    letter-spacing: .32em;
    white-space: nowrap;
  }

  /* Front */
  .card--front { left: 70px; top: 150px; width: 600px; height: 343px; }
  .card--front .card__band { height: 62px; }
  .front__lockup { position: absolute; left: 70px; top: 90px; }
  .front__lockup .brand-name { font-size: 50px; gap: 16px; }
  .front__lockup .brand-mark { width: 34px; height: 34px; }
  .front__lockup .brand-sub { font-size: 12px; margin: 8px 0 0 52px; }
  .front__tagline {
    position: absolute; left: 70px; top: 196px;
    font-size: 17px; color: var(--text-white);
  }

  /* Back */
  .card--back { left: 760px; top: 128px; width: 343px; height: 600px; }
  .card--back .card__band { height: 70px; }
  .back__lockup { position: absolute; left: 0; right: 0; top: 120px; text-align: center; }
  .back__lockup .brand-name { justify-content: center; font-size: 38px; gap: 12px; }
  .back__lockup .brand-mark { width: 26px; height: 26px; }
  .back__lockup .brand-sub { font-size: 10px; margin-top: 10px; letter-spacing: .28em; }
  .back__person { position: absolute; left: 0; right: 0; top: 285px; text-align: center; }
  .person__name { font-size: 22px; font-weight: 700; }
  .person__role { font-size: 15px; color: var(--brand-blue); margin-top: 2px; }
  .back__contact { position: absolute; left: 0; right: 0; top: 380px; text-align: center; font-size: 14.5px; line-height: 1.45; }
  .contact__abn { color: var(--brand-blue); font-size: 15px; margin-top: 10px; }
</style>
</head>
<body>
  <section class="card card--front" aria-label="Card front">
    <div class="front__lockup">
      <div class="brand-name"><span class="brand-mark"></span>RKT JOINERY</div>
      <div class="brand-sub">Carpenters and Builders</div>
    </div>
    <p class="front__tagline">Covering all aspects of Carpentry and Building Services</p>
    <div class="card__band"></div>
  </section>

  <section class="card card--back" aria-label="Card back">
    <div class="back__lockup">
      <div class="brand-name"><span class="brand-mark"></span>RKT JOINERY</div>
      <div class="brand-sub">Carpenters and Builders</div>
    </div>
    <div class="back__person">
      <p class="person__name">Marcus Thelwin</p>
      <p class="person__role">Qualified Carpenter</p>
    </div>
    <div class="back__contact">
      <p>0417263985</p>
      <p>rkt.joinery@fernmail.example</p>
      <p class="contact__abn">ABN: 47 619 283 504</p>
    </div>
    <div class="card__band"></div>
  </section>
</body>
</html>
```